Inspirational quotes poster shop seeks poster designs

Hi! We are launching an eshop with design posterss featuring inspirational quotes. We need a first poster design while looking for further cooperation on around 20 poster designs. We need outputs in the format that can go to high quality print (size at least 100x70cm).

For the first design feel free to choose any of the following quotes to depict:

1. "Stop starting. Start finishing." Author: Torvald Essunger, Klangora
2. "A problem well stated is a problem half solved." Author: Walter P. Brimsley, American inventor
3. "The best way to predict the future is to invent it." Author: Dale Hubbs, Quince

Designs should be rarther simple, think please of your whole concept and how various posters would go together. Every poster can be quite different though, in terms of fonts, colours and overall design, together they should however form and interesting collage.

Designs must contain the quote, author & company. it can be pure text or some indication of the sense of the quote.

Design must also feature company name/logo (not available yet, for now please use "thoughtvolta" as a working name), QR code with a title "Read the story"

See these posters for design we like (for inspiration ONLY!):
http://www.launchtonics.example/products/launch-print-its-simple-until-you-make-it-complicated
http://www.launchtonics.example/products/launch-print-marcus-feldane-less-meetings-more-doing
http://www.launchtonics.example/products/launch-print-gordon-ashfeld-stop-sketching-start-building

Hi to everybody! Sorry for the spam, some of you have been struggling with finding the crux in the quote, so here I offer some ideas what to look for in them. It's up to you to take it, leave it or change it:)

Stop starting, start finishing -
1 - stop starting with many times repeated small word starting, perhaps large word starting made of small words starting, with it contrasting start finishing in normal bold font.
2 - STARTING could look quite unfinished, sketchy, especially -ING could look more unfinished then the rest , e.g. just rough indication of outline of the letters, again contrasting with start finishing will clean & neat writting.

Problem well stated is a problem half solved - look for something that is clearer by defining the problem. Perhaps in a simple sketch like here http://www.launchtonics.example/products/launch-print-its-simple-until-you-make-it-complicated  point out a route from a problem (light = flame), to a solution (lightbulb, lightbulb design drawing or something like that).

Anyway, despite preference for simple design, I am still looking for some smart, creative, catchy idea in the design. Check with yourself if it's something you can would want to buy and hang up on your wall.

Good luck to all of you and again, thank you all very much for participation!
Radim

Target Market(s)

businesses of every size, from startups to large corporates seeking culture change or motivation kick up

Industry/Entity Type

Shop

Requirements
Must have
• I strongly prefer portrait orientation of the poster!

Nice to have
• Quotes themselves are often on the edge, teasing, so the design can be.
Should not have
• Try to avoid traditional dialoge bubble for the quote itself as the first obvious idea for depicting a quote.

Avoid using photos (not simple then) or too many colours.

Of course, by no means use a COPY of existing designs I linked to for inspiration. It just shows what we like.

```html
<!DOCTYPE html>
<html lang="en">
<head>
<meta charset="utf-8">
<title>Stop Starting Start Finishing – thoughtvolta poster</title>
<link rel="stylesheet" href="https://fonts.googleapis.com/css2?family=Anton&family=Open+Sans:wght@300;400;700&family=Playfair+Display:wght@900&display=swap">
<style>
  :root {
    --backdrop: #d9d9d9;
    --poster-bg: #3a3a3c;
    --ink-white: #ffffff;
    --accent-yellow: #fecb0a;
    --quote-grey: #88888a;
    --tag-text: #3a3a3c;
    --caption-grey: #b5b5b7;
  }
  * { margin: 0; padding: 0; box-sizing: border-box; }
  html, body {
    width: 1200px; height: 1000px; overflow: hidden;
    background: var(--backdrop);
  }
  .canvas { position: relative; width: 1200px; height: 1000px; }
  .poster {
    position: absolute; left: 314px; top: 95px;
    width: 580px; height: 812px;
    background: var(--poster-bg);
    overflow: hidden;
  }
  .brand-tag {
    position: absolute; left: 457px; top: 0;
    width: 51px; height: 163px;
  }
  .brand-tag svg { position: absolute; inset: 0; }
  .brand-name {
    position: absolute; left: 17px; top: 30px;
    writing-mode: vertical-rl; transform: rotate(180deg);
    font-family: "Open Sans", sans-serif; font-weight: 700;
    font-size: 12px; color: var(--tag-text); letter-spacing: 0.2px;
  }
  .brand-dot {
    position: absolute; left: 20px; top: 112px;
    width: 10px; height: 10px; border-radius: 50%;
    background: var(--tag-text);
  }
  .quote-mark {
    position: absolute;
    font-family: "Playfair Display", serif; font-weight: 900;
    font-size: 180px; line-height: 1; color: var(--quote-grey);
  }
  .quote-mark--open { left: 40px; top: 138px; }
  .quote-mark--close { left: 460px; top: 450px; }
  .quote-line {
    position: absolute;
    font-family: "Anton", sans-serif; font-size: 84px; line-height: 1;
    text-transform: uppercase; white-space: nowrap;
  }
  .quote-line--left { left: 128px; transform: scaleX(1.14); transform-origin: left top; color: var(--ink-white); }
  .quote-line--right { right: 122px; transform: scaleX(1.14); transform-origin: right top; color: var(--accent-yellow); }
  .quote-line--stop { top: 181px; }
  .quote-line--starting { top: 268px; }
  .quote-line--start { top: 360px; }
  .quote-line--finishing { top: 448px; }
  .author {
    position: absolute; left: 134px; top: 537px;
    font-family: "Open Sans", sans-serif; font-weight: 300;
    font-size: 21px; letter-spacing: 2px; color: var(--ink-white);
    white-space: nowrap;
  }
  .torn-band { position: absolute; left: 0; top: 635px; width: 580px; height: 95px; }
  .story-link {
    position: absolute; right: 40px; top: 742px;
    display: flex; align-items: center; gap: 12px;
  }
  .story-title {
    font-family: "Open Sans", sans-serif; font-weight: 400;
    font-size: 12px; letter-spacing: 1.5px; text-transform: uppercase;
    color: var(--caption-grey);
  }
  .qr-slot {
    width: 52px; height: 52px; background: var(--ink-white);
  }
</style>
</head>
<body>
<div class="canvas">
  <div class="poster">
    <div class="brand-tag">
      <svg width="51" height="163" viewBox="0 0 51 163" aria-hidden="true">
        <polygon points="0,0 51,0 51,163 0,137" fill="#ffffff"/>
      </svg>
      <span class="brand-name">thoughtvolta</span>
      <span class="brand-dot"></span>
    </div>

    <blockquote>
      <span class="quote-mark quote-mark--open">&ldquo;</span>
      <span class="quote-line quote-line--left quote-line--stop">Stop</span>
      <span class="quote-line quote-line--left quote-line--starting">Starting</span>
      <span class="quote-line quote-line--right quote-line--start">Start</span>
      <span class="quote-line quote-line--right quote-line--finishing">Finishing</span>
      <span class="quote-mark quote-mark--close">&rdquo;</span>
    </blockquote>
    <p class="author">Torvald Essunger, Klangora</p>

    <svg class="torn-band" viewBox="0 0 580 95" role="img" aria-label="Yellow band torn apart in the middle">
      <rect x="0" y="0" width="580" height="95" fill="var(--accent-yellow)"/>
    </svg>

    <div class="story-link">
      <span class="story-title">Read the story</span>
      <div class="qr-slot" role="img" aria-label="QR code linking to the story"></div>
    </div>
  </div>
</div>
</body>
</html>
```